Business Cards Real Estate Agent
Beach Real Estate Agent
Bright & Fun-filled
Gus Lindqvar
KT Real Estate Brokers
4870 Corvell St
Harbor Point, CA 90412
guslindqvar@postvane.net
http://www.guslindqvar.net
Logo and email address.
Please use this logo.
AI Logo
PDF Version

```html
<!DOCTYPE html>
<html lang="en">
<head>
<meta charset="utf-8">
<title>Gus Lindqvar – Business Cards</title>
<link href="https://fonts.googleapis.com/css2?family=Lato:wght@300;400;700&display=swap" rel="stylesheet">
<style>
  :root{
    --backdrop:#e6e7ea;
    --card:#4a5466;
    --card-deep:#3c4555;
    --ink:#ffffff;
    --ink-soft:#d9dde4;
    --silver:#c8ccd3;
    --silver-light:#eef0f3;
    --silver-dark:#8d939d;
  }
  *{margin:0;padding:0;box-sizing:border-box}
  html,body{width:1200px;height:787px;overflow:hidden}
  body{background:var(--backdrop);font-family:'Lato',sans-serif;color:var(--ink);position:relative}
  .card{position:absolute;top:238px;width:530px;height:310px;background:var(--card);border-radius:14px;overflow:hidden;box-shadow:0 10px 26px rgba(0,0,0,.25)}
  .card--front{left:45px}
  .card--back{left:625px}

  .brand{display:flex;align-items:center;gap:10px}
  .brand__dot{width:14px;height:14px;border-radius:50%;background:var(--silver);flex:none}
  .brand__name{font-weight:400;text-transform:uppercase;letter-spacing:2px;color:var(--ink);white-space:nowrap}

  .card--front .brand{position:absolute;left:34px;top:112px}
  .card--front .brand__name{font-size:25px}

  .divider-v{position:absolute;left:272px;top:48px;width:1px;height:120px;background:rgba(255,255,255,.35)}

  .contact{position:absolute;left:290px;top:44px;width:220px}
  .contact__name{font-size:17px;font-weight:700}
  .contact__company{font-size:11px;color:var(--ink-soft);margin-top:2px}
  .contact__rule{border-top:1px dotted rgba(255,255,255,.6);margin:9px 0 8px;width:120px}
  .contact__line{font-size:11px;color:var(--ink-soft);line-height:16px;display:flex;align-items:center;gap:6px;white-space:nowrap}
  .contact__line svg{width:10px;height:10px;flex:none}
  .contact__address{margin-bottom:8px}
  .contact__address .contact__line{padding-left:16px}

  .swoosh{position:absolute;left:0;bottom:0;width:530px;height:150px}
  .card--front .website{position:absolute;right:38px;top:186px;font-size:13px;font-weight:700;letter-spacing:.3px}

  .card--back .brand{position:absolute;left:0;right:0;top:118px;justify-content:center}
  .card--back .brand__name{font-size:30px}
  .card--back .rule{position:absolute;left:120px;right:120px;top:178px;height:1px;background:linear-gradient(90deg,transparent,var(--silver),transparent)}
  .card--back .website{position:absolute;left:0;right:0;top:196px;text-align:center;font-size:14px;font-weight:400;letter-spacing:.4px}
</style>
</head>
<body>

<section class="card card--front">
  <div class="brand">
    <span class="brand__dot"></span>
    <span class="brand__name">Gus Lindqvar</span>
  </div>

  <div class="divider-v"></div>

  <div class="contact">
    <p class="contact__name">Gus Lindqvar</p>
    <p class="contact__company">KT Real Estate Brokers</p>
    <div class="contact__rule"></div>
    <div class="contact__address">
      <p class="contact__line">4870 Corvell St</p>
      <p class="contact__line">Harbor Point, CA 90412</p>
    </div>
    <p class="contact__line">
      <svg viewBox="0 0 10 10"><rect x="2.5" y="0.5" width="5" height="9" rx="1" fill="none" stroke="#fff" stroke-width="1"/><circle cx="5" cy="7.8" r=".6" fill="#fff"/></svg>
      (310) 555-0148
    </p>
    <p class="contact__line">
      <svg viewBox="0 0 10 10"><rect x=".5" y="2" width="9" height="6" fill="none" stroke="#fff" stroke-width="1"/><path d="M.5 2 5 5.5 9.5 2" fill="none" stroke="#fff" stroke-width="1"/></svg>
      guslindqvar@postvane.net
    </p>
  </div>

  <svg class="swoosh" viewBox="0 0 530 150" preserveAspectRatio="none" aria-hidden="true">
    <defs>
      <linearGradient id="silverBand" x1="0" y1="0" x2="1" y2="0">
        <stop offset="0" stop-color="#8d939d"/>
        <stop offset=".35" stop-color="#eef0f3"/>
        <stop offset=".7" stop-color="#c8ccd3"/>
        <stop offset="1" stop-color="#8d939d"/>
      </linearGradient>
    </defs>
    <path d="M0 110 C120 150 260 140 360 95 C430 62 490 45 530 40 L530 150 L0 150 Z" fill="url(#silverBand)"/>
    <path d="M0 126 C130 160 270 150 370 110 C440 82 495 68 530 64 L530 150 L0 150 Z" fill="#3c4555"/>
    <path d="M0 140 C140 165 280 155 380 122 C445 100 500 88 530 86 L530 150 L0 150 Z" fill="#c8ccd3" opacity=".55"/>
  </svg>
  <p class="website">www.guslindqvar.net</p>
</section>

<section class="card card--back">
  <div class="brand">
    <span class="brand__dot"></span>
    <span class="brand__name">Gus Lindqvar</span>
  </div>
  <div class="rule"></div>
  <p class="website">www.guslindqvar.net</p>
</section>

</body>
</html>
```